Mendocino County Cannabis Business Needs Poster/Playbill Design for Event "Copper Ridge Gath...

Copper Ridge Gathering
Tall Pine Yield Ready Summit
Open House
-Date Thursday August 15
-Time 3-8pm
Phone Please RSVP @ 707-555-0147 or distribution@copperridgevalley.example
-Address 812 North Fern Lane Willits, CA 95490
Mendocino County
-Entertainment- Brightrune; Tidal Porch Quartet; Uncle Borvane

Are you a licensed operator or farmer in Mendocino County?
If so, We would like to invite you to a Tall Pine Yield Ready Summit, August 15th, hosted by Copper Ridge!

You are cordially invited to walk the yellow brick road and tour Copper Ridge's facility; Explore Copper Ridge's services and the chance to collaboratively source products.

Copper Ridge has all your post harvest needs.

Bring your market ready products and visions for your business.
Let's Make Plans for the most Important Quarter of the Year!

Live Entertainment; Tour; Service Scout; Networking; Good Times!

Event Collaborated By
(dusty meadow logo; pellaroot logo, verdo glow logo)

Here are links to Our Websites

https://copperridgevalley.example/about-us.html
https://www.dustymeadow.example
http://www.pellaroot.example

Target Market(s)

licensed mendocino county cannabis farmers and operators

Requirements
Nice to have
• not open to the public, licensed cannabis operators only, invite necessary,please rsvp

```html
<!DOCTYPE html>
<html lang="en">
<head>
<meta charset="utf-8">
<title>Tall Pine Yield Ready Summit – Copper Ridge Gathering</title>
<link rel="stylesheet" href="https://fonts.googleapis.com/css2?family=Kanit:wght@600;700&family=Montserrat:wght@400;600;700&family=Roboto:wght@400;700&display=swap">
<style>
  :root {
    --page: #ececec;
    --ink: #050505;
    --white: #ffffff;
    --yellow: #f2c12e;
    --green: #2fbf4f;
    --red: #ff2a1a;
    --blue: #2fa8e8;
    --lime: #b8d43a;
    --gold-band: #8a7033;
    --text-soft: #e6e6e6;
    --muted: #bdbdbd;
  }
  * { margin: 0; padding: 0; box-sizing: border-box; }
  html, body { width: 1200px; height: 830px; overflow: hidden; background: var(--page); }
  .poster {
    position: absolute; left: 315px; top: 12px; width: 570px; height: 806px;
    background: var(--ink); overflow: hidden; color: var(--white);
    font-family: "Roboto", Arial, sans-serif;
  }
  .scene {
    position: absolute; left: 0; top: 0; width: 570px; height: 560px;
    background: linear-gradient(180deg, #2a2a2a 0%, #9d9d9d 12%, #c9c9c9 24%, #8e8e86 40%, #4d4a35 58%, #2a2817 78%, var(--ink) 100%);
  }
  .moon {
    position: absolute; left: 187px; top: 17px; width: 194px; height: 194px;
    border-radius: 50%; background: radial-gradient(circle, #f4f6f3 0%, #e3e7e2 70%, #cfd4cf 100%);
  }
  .brand {
    position: absolute; left: 0; width: 570px; text-align: center;
    font-family: "Montserrat", sans-serif; font-weight: 700; color: #1f8a3c;
  }
  .brand-name { top: 130px; font-size: 22px; }
  .brand-sub { top: 160px; font-size: 12px; letter-spacing: 5px; }
  .headline { position: absolute; left: 0; width: 570px; text-align: center;
    font-family: "Kanit", sans-serif; font-weight: 700; line-height: 1;
    text-shadow: 0 3px 0 rgba(0,0,0,.55), 0 0 8px rgba(0,0,0,.4); letter-spacing: -1px; }
  .h-white { top: 222px; font-size: 70px; color: var(--white); }
  .h-yellow { top: 290px; font-size: 74px; color: var(--yellow); }
  .h-green { top: 364px; font-size: 72px; color: var(--green); }
  .band {
    position: absolute; left: 157px; top: 445px; width: 246px; height: 32px;
    background: var(--gold-band); border-radius: 3px;
    font-family: "Montserrat", sans-serif; font-size: 17px; letter-spacing: 6px;
    text-align: center; line-height: 32px; color: var(--white);
  }
  .divider { position: absolute; left: 266px; top: 495px; width: 1px; height: 262px; background: var(--white); opacity: .8; }
  .date-day, .date-month { position: absolute; left: 54px; font-family: "Montserrat", sans-serif; letter-spacing: 8px; }
  .date-day { top: 496px; font-size: 15px; color: var(--muted); }
  .date-month { top: 572px; font-size: 23px; letter-spacing: 9px; font-weight: 600; }
  .date-num { position: absolute; left: 50px; top: 508px; font-family: "Kanit", sans-serif; font-weight: 700; font-size: 72px; line-height: 1; color: var(--yellow); letter-spacing: -1px; }
  .date-year { position: absolute; left: 228px; top: 495px; width: 18px; font-family: "Montserrat", sans-serif; font-weight: 700; font-size: 20px; line-height: 25px; color: #2d2d2d; text-align: center; }
  .info { position: absolute; left: 54px; display: flex; align-items: center; gap: 8px; }
  .info svg { flex: none; }
  .time { top: 609px; font-family: "Montserrat", sans-serif; font-size: 24px; }
  .address { top: 642px; font-size: 12.5px; line-height: 15px; }
  .rsvp { position: absolute; left: 78px; top: 682px; font-size: 9.5px; }
  .phone { top: 697px; font-family: "Montserrat", sans-serif; font-weight: 700; font-size: 20px; color: var(--yellow); }
  .email { top: 720px; font-size: 10.5px; }
  .notice { position: absolute; left: 54px; top: 741px; width: 215px; font-size: 8.8px; line-height: 11px; color: var(--lime); }
  .details { position: absolute; left: 284px; top: 494px; width: 250px; font-size: 10.5px; line-height: 13.5px; }
  .details p { margin-bottom: 5px; }
  .accent { color: var(--yellow); font-weight: 700; }
  .accent-lg { color: var(--yellow); font-size: 13px; line-height: 17px; font-family: "Montserrat", sans-serif; font-weight: 600; }
  .activities { font-family: "Montserrat", sans-serif; font-weight: 700; font-size: 14.5px; line-height: 19px; margin-top: 9px; }
  .yellow { color: var(--yellow); } .red { color: var(--red); } .blue { color: var(--blue); } .green { color: var(--green); }
  .credit-label { position: absolute; top: 741px; font-size: 7.5px; color: var(--text-soft); }
  .credit-ent { left: 357px; } .credit-collab { left: 452px; }
  .sponsor { position: absolute; display: flex; align-items: center; gap: 3px; font-family: "Roboto", sans-serif; font-weight: 700; font-size: 8px; color: var(--yellow); }
  .sponsor i { width: 9px; height: 9px; border-radius: 50%; background: var(--white); flex: none; }
</style>
</head>
<body>
  <main class="poster">
    <div class="scene" role="img" aria-label="Misty mountain range with pine forest silhouettes under a cloudy grey sky"></div>
    <div class="moon" role="img" aria-label="Full moon"></div>
    <div class="brand brand-name">COPPER RIDGE</div>
    <div class="brand brand-sub">GATHERING</div>

    <h1>
      <span class="headline h-white">TALL PINE</span>
      <span class="headline h-yellow">YIELD READY</span>
      <span class="headline h-green">SUMMIT</span>
    </h1>

    <div class="band">OPEN HOUSE</div>

    <div class="date-day">THURSDAY</div>
    <div class="date-num">15TH</div>
    <div class="date-month">AUGUST</div>
    <div class="date-year">2<br>0<br>1<br>9</div>

    <div class="info time">
      <svg width="16" height="16" viewBox="0 0 16 16"><circle cx="8" cy="8" r="6.5" fill="none" stroke="#2fbf4f" stroke-width="1.6"/><path d="M8 4v4.3l2.6 1.6" fill="none" stroke="#2fbf4f" stroke-width="1.6"/></svg>
      <span>TIME : 3-8 PM</span>
    </div>
    <div class="info address">
      <svg width="16" height="20" viewBox="0 0 16 20"><path d="M8 1a6 6 0 0 1 6 6c0 4.5-6 12-6 12S2 11.5 2 7a6 6 0 0 1 6-6z" fill="#2fbf4f"/><circle cx="8" cy="7" r="2.3" fill="#050505"/></svg>
      <span>812 North Fern Lane Willits, CA<br>95490, Mendocino County</span>
    </div>
    <div class="rsvp">RSVP ONLY</div>
    <div class="info phone">
      <svg width="16" height="16" viewBox="0 0 16 16"><circle cx="8" cy="8" r="8" fill="#2fbf4f"/><path d="M5.2 4.2l1.4-.3 1 2.2-.9.8c.5 1.1 1.3 1.9 2.4 2.4l.8-.9 2.2 1-.3 1.4C9.5 12 4 6.5 5.2 4.2z" fill="#050505"/></svg>
      <span>707-555-0147</span>
    </div>
    <div class="info email">
      <svg width="14" height="10" viewBox="0 0 14 10"><rect x=".6" y=".6" width="12.8" height="8.8" fill="none" stroke="#2fbf4f" stroke-width="1.2"/><path d="M.6.6 7 5.6 13.4.6" fill="none" stroke="#2fbf4f" stroke-width="1.2"/></svg>
      <span>distribution@copperridgevalley.example</span>
    </div>
    <p class="notice">Licensed Cannabis Operators Only, Not Open to the Public, Invite Necessary, Please RSVP</p>

    <div class="divider"></div>

    <section class="details">
      <p>You are cordially invited to walk the yellow brick road and tour Copper Ridge's facility; Explore Copper Ridge's services and the chance to collaboratively source products.</p>
      <p class="accent">COPPER RIDGE HAS ALL YOUR POST HARVEST NEEDS.</p>
      <p>Bring your market ready products and visions for your business.</p>
      <p class="accent-lg">LET'S MAKE PLANS FOR THE MOST IMPORTANT QUARTER OF THE YEAR!</p>
      <p class="activities"><span class="yellow">LIVE ENTERTAINMENT</span><br>TOUR, <span class="red">SERVICE SCOUT,</span><br><span class="blue">NETWORKING,</span> <span class="green">GOOD TIMES!</span></p>
    </section>

    <div class="credit-label credit-ent">Entertainment</div>
    <div class="credit-label credit-collab">Event&nbsp; Collaborated By</div>
    <div class="sponsor" style="left:346px;top:758px;">Brightrune</div>
    <div class="sponsor" style="left:346px;top:776px;">Uncle Borvane</div>
    <div class="sponsor" style="left:432px;top:767px;"><i></i>dusty meadow</div>
    <div class="sponsor" style="left:492px;top:757px;"><i></i>pellaroot</div>
    <div class="sponsor" style="left:492px;top:777px;"><i></i>verdo glow</div>
  </main>
</body>
</html>
```